Quandell USA PowerPoint Template

I need a generic PPT template for my business, need to incorporate my logo and colors, need a professional look, master slide should have a title bar at top with logo right, a light logo watermark on the body section, and a page number at the bottom of each page. I've attached the first presentation for this template, but I'll use this template for all company presentations.

Target Market(s)

Investors, clients.

Font styles to use
Sans Serif
Other font styles liked:
• You choose. Professional and modern.

```html
<!DOCTYPE html>
<html lang="en">
<head>
<meta charset="utf-8">
<title>Quandell USA — Presentation Template</title>
<link href="https://fonts.googleapis.com/css2?family=Poppins:wght@300;400;500;600;700;800&display=swap" rel="stylesheet">
<style>
:root{
  --navy:#101a45;
  --navy-deep:#0a1233;
  --red:#c8081c;
  --red-dark:#7e0410;
  --ink:#1b1f2e;
  --muted:#4a4f60;
  --board:#c4c4c4;
  --white:#ffffff;
  --line:#3a3a3a;
  --ghost:rgba(16,26,69,.06);
}
*{margin:0;padding:0;box-sizing:border-box}
html,body{width:985px;height:1200px;overflow:hidden;background:var(--board)}
body{font-family:"Poppins",Arial,sans-serif;color:var(--ink)}
.board{position:absolute;left:0;top:0;width:1736px;height:2116px;transform:scale(.5674);transform-origin:0 0}
.slide{position:absolute;width:726px;height:409px;background:var(--white);overflow:hidden;box-shadow:0 1px 3px rgba(0,0,0,.15)}
.col-a{left:103px}.col-b{left:907px}
.row-1{top:100px}.row-2{top:593px}.row-3{top:1087px}.row-4{top:1580px}
.abs{position:absolute}

/* body watermark */
.watermark{position:absolute;left:248px;top:92px;width:230px;height:240px;display:flex;flex-direction:column;align-items:center;justify-content:center;gap:14px;pointer-events:none}
.watermark-square{width:150px;height:150px;border:14px solid var(--ghost)}
.watermark-name{font-size:24px;font-weight:800;color:var(--ghost);white-space:nowrap;letter-spacing:.5px}

/* header */
.title-bar{position:absolute;left:0;top:0;width:17px;height:53px;background:var(--red)}
.slide-title{position:absolute;left:35px;top:12px;font-size:25px;font-weight:700;color:var(--navy);letter-spacing:.2px;white-space:nowrap}
.slide-title em{font-style:normal;color:var(--red)}
.brand{position:absolute;right:36px;top:17px;display:flex;align-items:center;gap:6px}
.brand-mark{width:20px;height:20px;background:var(--navy)}
.brand-name{font-size:16px;font-weight:800;color:var(--navy);letter-spacing:.2px;white-space:nowrap}

/* footer */
.footer{position:absolute;left:0;bottom:0;width:726px;height:29px;background:linear-gradient(100deg,var(--white) 0,var(--white) 140px,var(--navy-deep) 150px,var(--navy) 100%)}
.page-label{position:absolute;left:35px;top:7px;font-size:9px;font-weight:700;color:var(--navy);display:flex;align-items:center;gap:4px}
.page-num{width:19px;height:19px;border-radius:50%;background:var(--red);color:var(--white);font-size:8px;display:flex;align-items:center;justify-content:center}
.copyright{position:absolute;right:37px;top:9px;font-size:8px;font-weight:700;color:var(--white)}

/* cover */
.cover{background:radial-gradient(circle at 30% 40%,#1a2458 0,#0c1540 55%,#08102f 100%)}
.cover-frame{position:absolute;left:52px;top:92px;width:252px;height:252px;border:16px solid var(--white)}
.cover-brand{position:absolute;left:393px;top:103px;display:flex;align-items:center;gap:8px}
.cover-brand .brand-name{font-size:32px;color:var(--white)}
.cover-title{position:absolute;left:393px;top:175px;font-size:36px;line-height:49px;font-weight:800;color:var(--white)}
.cover-date{position:absolute;left:393px;top:285px;font-size:18px;font-weight:800;color:var(--red)}

/* text helpers */
.lead{font-size:11.5px;line-height:17px;color:var(--ink)}
.point{display:flex;gap:8px;font-size:10.5px;line-height:15px;font-weight:500}
.tick{flex:0 0 12px;width:12px;height:12px;margin-top:2px;background:var(--navy);border:2px solid var(--red)}
.dots{list-style:none}
.dots li{position:relative;padding-left:15px;font-size:8.6px;line-height:19px;color:var(--ink)}
.dots li::before{content:"";position:absolute;left:2px;top:6px;width:6px;height:6px;border-radius:50%;background:var(--red)}
.phase{font-size:10.5px;font-weight:600;color:var(--navy)}
.phase em{font-style:normal;color:var(--red)}

/* market overview */
.panel{position:absolute;top:118px;width:306px;height:226px;border:7px solid var(--navy);padding:24px 12px 0 12px;background:transparent}
.panel-tag{position:absolute;top:-22px;height:30px;padding:0 16px;border-radius:16px 16px 0 0;color:var(--white);font-size:12.5px;display:flex;align-items:center}
.panel-item{display:flex;gap:6px;margin-bottom:8px}
.panel-item p{font-size:7.4px;line-height:12px;color:var(--muted)}
.panel-item b{font-size:9.5px;font-weight:600;color:var(--ink)}

/* advantages */
.adv{position:absolute;display:flex;align-items:flex-start;gap:10px;width:320px}
.adv-icon{flex:0 0 38px;width:38px;height:38px;border-radius:50%;display:flex;align-items:center;justify-content:center}
.adv-icon.navy{background:var(--navy)}
.adv-icon.red{background:var(--red)}
.adv h3{font-size:13.5px;font-weight:500;color:var(--navy);line-height:17px}
.adv p{font-size:8.5px;color:var(--muted);line-height:12px;margin-top:4px}

/* business plan */
.plan{position:absolute;left:35px;display:flex;gap:10px;width:300px}
.plan-icon{flex:0 0 34px;width:34px;height:34px;border-radius:50%;border:2px solid var(--navy);display:flex;align-items:center;justify-content:center}
.plan h3{font-size:11px;font-weight:600;color:var(--ink);line-height:16px}
.plan p{font-size:8.2px;line-height:13px;color:var(--muted);margin-top:4px}
.photo-frame{position:absolute;left:383px;top:72px;width:306px;height:265px;border:6px solid var(--navy);background:var(--white)}
.photo{position:absolute;left:10px;top:8px;right:10px;bottom:8px;background:radial-gradient(circle at 75% 30%,#f3d78a 0,#e6e2d8 25%,#cfcfcf 70%,#b9b9b9 100%)}

/* revenue */
.chart{position:absolute;top:72px;width:252px;height:158px;background:var(--white);border:3px solid var(--navy)}
.chart.red{border-color:var(--red)}
.rev-point{position:absolute;width:260px;font-size:9.5px;line-height:15px}

/* cash table */
.cash{position:absolute;left:36px;top:83px;width:647px;border-collapse:collapse;font-size:8.8px;background:var(--white)}
.cash th{height:37px;color:var(--white);font-size:12.5px;font-weight:600;background:linear-gradient(90deg,var(--red-dark),var(--red))}
.cash td{height:31px;border:1px solid var(--line);padding:0 3px;color:var(--ink)}
.cash td.cost{text-align:right}
.cash td.cost span{float:left}
.cash tr.total td{font-weight:700}
</style>
</head>
<body>
<div class="board">

  <!-- 1 Cover -->
  <section class="slide cover col-a row-1">
    <div class="cover-frame"></div>
    <div class="cover-brand"><span class="brand-name">QUANDELL USA</span></div>
    <h1 class="cover-title">PRESENTATION<br>TITLE HERE</h1>
    <p class="cover-date">JUNE 06,2025</p>
  </section>

  <!-- 2 Situational overview -->
  <section class="slide col-b row-1">
    <div class="watermark" aria-hidden="true"><span class="watermark-square"></span><span class="watermark-name">QUANDELL USA</span></div>
    <div class="title-bar"></div>
    <h2 class="slide-title">SITUATIONAL <em>OVERVIEW</em></h2>
    <div class="brand"><span class="brand-mark"></span><span class="brand-name">QUANDELL USA</span></div>
    <div class="abs" style="left:35px;top:52px;width:320px">
      <p class="lead">Quandell USA is the exclusive distributor in North America for Anatolia Fiber Reinforced Resins Composite Technologies of Turkey.</p>
      <div class="point" style="margin-top:12px"><span class="tick"></span><span>Product portfolio includes:</span></div>
      <ul class="dots" style="margin:6px 0 0 12px">
        <li>Fiber Reinforced Plastic (FRP) Grating.</li>
        <li>FRP Laminated Sheet.</li>
        <li>FRP Pultruded Shapes.</li>
        <li>FRP Compression Molded Shapes.</li>
      </ul>
      <div class="point" style="margin-top:12px;width:270px"><span class="tick"></span><span>All products are manufactured at the Quandell factory near the Port of Izmir, Turkey.</span></div>
      <div class="point" style="margin-top:15px;width:270px"><span class="tick"></span><span>Quandell Anatolia is wholly owned by Mr. Kerem Aslan.</span></div>
      <div class="point" style="margin-top:15px;width:270px"><span class="tick"></span><span>Quandell USA is jointly owned by Kerem Aslan and Dana Whitfield.</span></div>
    </div>
    <div class="abs" style="left:383px;top:52px;width:310px">
      <p class="lead">The U.S. business plan is being<br>executed in two phases:</p>
      <div class="point" style="margin-top:10px"><span class="tick"></span><span class="phase">Phase 1 – <em>Market Intelligence</em></span></div>
      <ul class="dots" style="margin-top:6px">
        <li>Proven product-market fit with 4 large recurring customers.</li>
        <li>Gained deep understanding of the U.S. and Americas market.</li>
        <li>Identified and addressed testing &amp; certification requirements.</li>
        <li>Specified custom tooling to meet U.S. standards.</li>
        <li>Developed a full set of sales &amp; technical materials in imperial units.</li>
        <li>Identified clear competitive differentiators.</li>
      </ul>
      <div class="point" style="margin-top:12px"><span class="tick"></span><span class="phase">Phase 2 – <em>Growth</em></span></div>
      <ul class="dots" style="margin-top:6px"><li>Now preparing to fund and scale the business.</li></ul>
    </div>
    <div class="footer"><div class="page-label">PAGE NUMBER: <span class="page-num">02</span></div><p class="copyright">Copyrights@2025.Company Name.All Rights Reserved</p></div>
  </section>

  <!-- 3 Market overview -->
  <section class="slide col-a row-2">
    <div class="watermark" aria-hidden="true"><span class="watermark-square"></span><span class="watermark-name">QUANDELL USA</span></div>
    <div class="title-bar"></div>
    <h2 class="slide-title">US FRP <em>MARKET OVERVIEW</em></h2>
    <div class="brand"><span class="brand-mark"></span><span class="brand-name">QUANDELL USA</span></div>
    <p class="abs" style="left:35px;top:50px;width:640px;font-size:12.5px;line-height:21px;font-weight:300"><b style="font-weight:600">US Market Size (2024):</b> Estimated at $24.03 billion, with projections to reach $43.67 billion by 2032, reflecting a Compound Annual Growth Rate (CAGR) of 7.6%.</p>
    <div class="panel" style="left:37px">
      <span class="panel-tag" style="left:60px;background:var(--navy)">Key Growth Drivers:</span>
      <div class="panel-item"><span class="tick" style="margin-top:1px"></span><p><b>Automotive Sector:</b> Increasing demand for lightweight, fuel-efficient vehicles is driving the adoption of FRP composites.</p></div>
      <div class="panel-item"><span class="tick" style="margin-top:1px"></span><p><b>Aerospace Industry:</b> FRP materials are favored for their high strength-to-weight ratio, contributing to improved aircraft performance.</p></div>
      <div class="panel-item"><span class="tick" style="margin-top:1px"></span><p><b>Construction &amp; Infrastructure:</b> FRP's corrosion resistance and durability make it ideal for bridges, pipelines, and building reinforcements.</p></div>
      <div class="panel-item"><span class="tick" style="margin-top:1px"></span><p><b>Marine Applications:</b> FRP's resistance to moisture and chemicals enhances its suitability for shipbuilding and offshore structures.</p></div>
    </div>
    <div class="panel" style="left:382px">
      <span class="panel-tag" style="left:60px;background:var(--red)">Recent Developments:</span>
      <div class="panel-item"><span class="tick" style="margin-top:1px"></span><p><b>Infrastructure Investments:</b> The U.S. government's focus on infrastructure modernization is boosting the demand for FRP materials in construction projects.</p></div>
      <div class="panel-item" style="margin-top:10px"><span class="tick" style="margin-top:1px"></span><p><b>Sustainability Initiatives:</b> There's a growing emphasis on developing recyclable and bio-based FRP composites to meet environmental regulations.</p></div>
      <div class="panel-item" style="margin-top:10px"><span class="tick" style="margin-top:1px"></span><p><b>Technological Advancements:</b> Innovations in manufacturing processes, such as resin transfer molding (RTM) and pultrusion, are enhancing production efficiency and product quality.</p></div>
    </div>
    <div class="footer"><div class="page-label">PAGE NUMBER: <span class="page-num">03</span></div><p class="copyright">Copyrights@2025.Company Name.All Rights Reserved</p></div>
  </section>

  <!-- 4 Market advantages -->
  <section class="slide col-b row-2">
    <div class="watermark" aria-hidden="true"><span class="watermark-square"></span><span class="watermark-name">QUANDELL USA</span></div>
    <div class="title-bar"></div>
    <h2 class="slide-title">QUANDELL <em>MARKET ADVANTAGES</em></h2>
    <div class="brand"><span class="brand-mark"></span><span class="brand-name">QUANDELL USA</span></div>
    <div class="adv" style="left:35px;top:68px"><span class="adv-icon navy"><svg width="18" height="18" viewBox="0 0 18 18" fill="none" stroke="#fff" stroke-width="1.4"><circle cx="9" cy="9" r="4"/><path d="M9 1v3M9 14v3M1 9h3M14 9h3"/></svg></span><div><h3>Market Advantages</h3><p>Improved pricing flexibility.</p></div></div>
    <div class="adv" style="left:35px;top:131px"><span class="adv-icon navy"><svg width="18" height="18" viewBox="0 0 18 18" fill="none" stroke="#fff" stroke-width="1.4"><path d="M3 15h12M5 15V8M9 15V5M13 15V9"/></svg></span><div><h3>Unusually Broad FRP Product Line</h3><p>"One-stop Shop"</p></div></div>
    <div class="adv" style="left:35px;top:196px;width:330px"><span class="adv-icon navy"><svg width="18" height="18" viewBox="0 0 18 18" fill="none" stroke="#fff" stroke-width="1.4"><path d="M3 9l6-6h6v6l-6 6z"/><circle cx="12" cy="6" r="1"/></svg></span><div><h3>Stable and Transparent Pricing</h3><p>Allows for online ordering with no need for<br><b style="color:var(--ink);font-weight:600">"Request a Quote"</b></p></div></div>
    <div class="adv" style="left:35px;top:273px;width:330px"><span class="adv-icon navy"><svg width="18" height="18" viewBox="0 0 18 18" fill="none" stroke="#fff" stroke-width="1.4"><circle cx="9" cy="10" r="5"/><path d="M9 2v3M6 10h6"/></svg></span><div><h3>Dual Channel Sales</h3><p>Wholesale (by cargo container) &amp; Retail (small lots)</p></div></div>
    <div class="adv" style="left:380px;top:68px"><span class="adv-icon red"><svg width="18" height="18" viewBox="0 0 18 18" fill="none" stroke="#fff" stroke-width="1.4"><path d="M3 15h12M5 15v-3M9 15V8M13 15V4"/></svg></span><div><h3>U.S. Market Presence</h3><p>Clients often reference superior customer service</p></div></div>
    <div class="adv" style="left:380px;top:128px;width:320px"><span class="adv-icon red"><svg width="18" height="18" viewBox="0 0 18 18" fill="none" stroke="#fff" stroke-width="1.4"><rect x="4" y="3" width="10" height="12"/><path d="M6 7h6M6 10h4"/></svg></span><div><h3>Cost Advantage from Turkish Supply Chain Advantages</h3><p>Competitive costs with China and India<br>competitors</p></div></div>
    <div class="adv" style="left:380px;top:211px"><span class="adv-icon red"><svg width="18" height="18" viewBox="0 0 18 18" fill="none" stroke="#fff" stroke-width="1.4"><path d="M9 16s5-5 5-9a5 5 0 0 0-10 0c0 4 5 9 5 9z"/><circle cx="9" cy="7" r="2"/></svg></span><div><h3>Favorable U.S. Tariff Position</h3><p>Superior position to China competitors</p></div></div>
    <div class="adv" style="left:380px;top:280px;width:330px"><span class="adv-icon red"><svg width="18" height="18" viewBox="0 0 18 18" fill="none" stroke="#fff" stroke-width="1.4"><rect x="3" y="6" width="12" height="8" rx="1"/><path d="M6 6V4h6v2"/></svg></span><div><h3>Lower fixed costs</h3><p>Automate &amp; leverage AI to reduce the need for staff.</p></div></div>
    <div class="footer"><div class="page-label">PAGE NUMBER: <span class="page-num">04</span></div><p class="copyright">Copyrights@2025.Company Name.All Rights Reserved</p></div>
  </section>

  <!-- 5 Section divider -->
  <section class="slide col-a row-3">
    <div class="watermark" aria-hidden="true"><span class="watermark-square"></span><span class="watermark-name">QUANDELL USA</span></div>
    <div class="title-bar"></div>
    <h2 class="slide-title">SECTION <em>DIVIDER</em></h2>
    <div class="brand"><span class="brand-mark"></span><span class="brand-name">QUANDELL USA</span></div>
    <div class="footer"><div class="page-label">PAGE NUMBER: <span class="page-num">05</span></div><p class="copyright">Copyrights@2025.Company Name.All Rights Reserved</p></div>
  </section>

  <!-- 6 Business plan overview -->
  <section class="slide col-b row-3">
    <div class="watermark" aria-hidden="true"><span class="watermark-square"></span><span class="watermark-name">QUANDELL USA</span></div>
    <div class="title-bar"></div>
    <h2 class="slide-title">BUSINESS <em>PLAN OVERVIEW</em></h2>
    <div class="brand"><span class="brand-mark"></span><span class="brand-name">QUANDELL USA</span></div>
    <div class="plan" style="top:72px"><span class="plan-icon"><svg width="16" height="16" viewBox="0 0 16 16" fill="none" stroke="#101a45" stroke-width="1.3"><circle cx="7" cy="7" r="5"/><path d="M11 11l4 4"/></svg></span><div><h3>Address South Florida Market to Prove Operations</h3><p>Focus on construction industry.</p></div></div>
    <div class="plan" style="top:140px;width:310px"><span class="plan-icon"><svg width="16" height="16" viewBox="0 0 16 16" fill="none" stroke="#101a45" stroke-width="1.3"><circle cx="8" cy="8" r="6"/><path d="M2 8h12M8 2c3 3 3 9 0 12M8 2c-3 3-3 9 0 12"/></svg></span><div><h3>Strong Web Presence</h3><p>Searchly ads, Searchly Storefront, Shopmart Storefront, etc.</p></div></div>
    <div class="plan" style="top:193px;width:310px"><span class="plan-icon"><svg width="16" height="16" viewBox="0 0 16 16" fill="none" stroke="#101a45" stroke-width="1.3"><circle cx="8" cy="8" r="3"/><path d="M8 1v3M8 12v3M1 8h3M12 8h3"/></svg></span><div><h3>Strong Technological Base</h3><p>Online store provide real time pricing (almost all large competitors require request a quote), integrated inventory control and accounting.</p></div></div>
    <div class="plan" style="top:276px;width:310px"><span class="plan-icon"><svg width="16" height="16" viewBox="0 0 16 16" fill="none" stroke="#101a45" stroke-width="1.3"><path d="M2 14V6l6-4 6 4v8zM5 14V9h6v5"/></svg></span><div><h3>Inventory &amp; Warehouse</h3><p>Begin with inventory focused on key products and scale to match market demand.&nbsp;&nbsp; Lease warehouse to support scaled inventory.</p></div></div>
    <div class="photo-frame"><div class="photo" role="img" aria-label="Photo of a thoughtful businesswoman beside a wall sketched with business plan doodles and a glowing light bulb"></div></div>
    <div class="footer"><div class="page-label">PAGE NUMBER: <span class="page-num">06</span></div><p class="copyright">Copyrights@2025.Company Name.All Rights Reserved</p></div>
  </section>

  <!-- 7 Revenue forecast -->
  <section class="slide col-a row-4">
    <div class="watermark" aria-hidden="true"><span class="watermark-square"></span><span class="watermark-name">QUANDELL USA</span></div>
    <div class="title-bar"></div>
    <h2 class="slide-title">REVENUE <em>FORECAST</em></h2>
    <div class="brand"><span class="brand-mark"></span><span class="brand-name">QUANDELL USA</span></div>
    <div class="chart" style="left:89px">
      <svg width="246" height="152" viewBox="0 0 246 152" font-family="Poppins, sans-serif">
        <text x="123" y="9" font-size="4.5" text-anchor="middle" fill="#555">Monthly Revenue Mix by Product Type</text>
        <g font-size="2.8" fill="#777" text-anchor="end"><text x="26" y="19">$2,500,000</text><text x="26" y="42">$2,000,000</text><text x="26" y="64">$1,500,000</text><text x="26" y="87">$1,000,000</text><text x="26" y="110">$500,000</text><text x="26" y="132">$-</text></g>
        <g font-size="2.8" fill="#555"><rect x="53" y="42" width="2" height="2" fill="#6a8ad0"/><text x="57" y="44">Total Monthly Revenue (Grating)</text><rect x="53" y="47" width="2" height="2" fill="#c06a6a"/><text x="57" y="49">Total Monthly Revenue (Sheet)</text><rect x="53" y="52" width="2" height="2" fill="#9ec27a"/><text x="57" y="54">Total Monthly Revenue (Pultrusion)</text></g>
        <polygon points="32,130 32,118 70,110 110,100 150,88 190,72 240,44 240,130" fill="#9ec27a"/>
        <polygon points="32,130 32,121 70,114 110,105 150,95 190,82 240,60 240,130" fill="#c06a6a"/>
        <polygon points="32,130 32,127 70,125 110,122 150,118 190,114 240,106 240,130" fill="#6a8ad0"/>
        <line x1="30" y1="130" x2="242" y2="130" stroke="#bbb" stroke-width=".5"/>
      </svg>
    </div>
    <div class="chart red" style="left:377px">
      <svg width="246" height="152" viewBox="0 0 246 152" font-family="Poppins, sans-serif">
        <text x="123" y="9" font-size="4.5" text-anchor="middle" fill="#555">Monthly Revenue Mix by Product Type</text>
        <g font-size="2.8" fill="#777" text-anchor="end"><text x="26" y="19">$2,500,000</text><text x="26" y="42">$2,000,000</text><text x="26" y="64">$1,500,000</text><text x="26" y="87">$1,000,000</text><text x="26" y="110">$500,000</text><text x="26" y="132">$-</text></g>
        <g font-size="2.8" fill="#555"><rect x="53" y="42" width="2" height="2" fill="#6a8ad0"/><text x="57" y="44">Total Monthly Revenue (Grating)</text><rect x="53" y="47" width="2" height="2" fill="#c06a6a"/><text x="57" y="49">Total Monthly Revenue (Sheet)</text><rect x="53" y="52" width="2" height="2" fill="#9ec27a"/><text x="57" y="54">Total Monthly Revenue (Pultrusion)</text></g>
        <polygon points="32,130 32,118 70,110 110,100 150,88 190,72 240,44 240,130" fill="#9ec27a"/>
        <polygon points="32,130 32,121 70,114 110,105 150,95 190,82 240,60 240,130" fill="#c06a6a"/>
        <polygon points="32,130 32,127 70,125 110,122 150,118 190,114 240,106 240,130" fill="#6a8ad0"/>
        <line x1="30" y1="130" x2="242" y2="130" stroke="#bbb" stroke-width=".5"/>
      </svg>
    </div>
    <div class="point rev-point" style="left:87px;top:256px"><span class="tick"></span><span>Revenue Growth to $1M/Month ($12M/year) over one year.</span></div>
    <div class="point rev-point" style="left:87px;top:301px"><span class="tick"></span><span>Revenue Growth to $1.9M/Month ($23M/year) over two years.</span></div>
    <div class="point rev-point" style="left:375px;top:256px"><span class="tick"></span><span>Sales mix approximately 33% Wholesale, 67% Retail.</span></div>
    <div class="point rev-point" style="left:375px;top:301px"><span class="tick"></span><span>Sales mix approximately 34% Grating, 57% Sheet (coil &amp; pallet), 8% Pultrusion.</span></div>
    <div class="footer"><div class="page-label">PAGE NUMBER: <span class="page-num">07</span></div><p class="copyright">Copyrights@2025.Company Name.All Rights Reserved</p></div>
  </section>

  <!-- 8 Cash needs -->
  <section class="slide col-b row-4">
    <div class="watermark" aria-hidden="true"><span class="watermark-square"></span><span class="watermark-name">QUANDELL USA</span></div>
    <div class="title-bar"></div>
    <h2 class="slide-title">CASH <em>NEEDS</em></h2>
    <div class="brand"><span class="brand-mark"></span><span class="brand-name">QUANDELL USA</span></div>
    <table class="cash">
      <colgroup><col style="width:177px"><col style="width:90px"><col></colgroup>
      <thead><tr><th>ITEM</th><th>E.COST</th><th>NOTES</th></tr></thead>
      <tbody>
        <tr><td>Starter Inventory</td><td class="cost"><span>$</span>150,000</td><td>Initial procurement of FRP products across all categories</td></tr>
        <tr><td>Pallet Racking (for ~185 pallets)</td><td class="cost"><span>$</span>45,000</td><td>Approx. $240 per pallet position (185 pallets)</td></tr>
        <tr><td>Small Forklift</td><td class="cost"><span>$</span>25,000</td><td>Includes charger; suitable for indoor, narrow-aisle use</td></tr>
        <tr><td>Warehouse Lease (initial payment)</td><td class="cost"><span>$</span>30,000</td><td style="line-height:12px">Typical commercial lease: first month, last month, and 1-month deposit <i>(est. $10,000/mo for ~6,000 sq ft)</i></td></tr>
        <tr><td>Working Capital &amp; Contingency</td><td class="cost"><span>$</span>100,000</td><td>For hiring, trade shows, marketing, and early operating costs</td></tr>
        <tr class="total"><td>Totals</td><td class="cost"><span>$</span>350,000</td><td></td></tr>
      </tbody>
    </table>
    <div class="footer"><div class="page-label">PAGE NUMBER: <span class="page-num">08</span></div><p class="copyright">Copyrights@2025.Company Name.All Rights Reserved</p></div>
  </section>

</div>
</body>
</html>
```